Fitness Clothing Apparel Business Card

This project is linked to Fitness Clothing Apparel, KESTREL, Looking for AWESOME Logo Design!!!.

Our company needs a Business Card Design. Please refer to our original project in the link above.

Hi, I'm looking for a professional logo design which will help brand my clothing and nutrition supplement company. The winner of this contest may be hired again in the future to help design some flyers, banners, graphics, etc.

A little background about the company...
KESTREL Fitness is a new fitness clothing and nutrition company based in Southern California... near the mecca of bodybuilding, Harlow Strand! Our company is based around the culture of fitness and bodybuilding. We design clothing that are functional yet appealing for an athletic individual.

What I would like to see on business card...
The card has communicate our brand values. It needs to have attitude yet professionally done. Our brand colors are black, red, and white.

Target Market(s)

Fitness and bodybuilding enthusiasts

Industry/Entity Type

Nutrition

Font styles to use
Serif
Sans Serif
Decorative
Script

Colors

Designer to choose colors to be used in the design.

Requirements
Must have
• our company logo
Nice to have
• red and black, an abstract design of a bull
Should not have
• I'm open to all ideas, appearance is important

```html
<!DOCTYPE html>
<html lang="en">
<head>
<meta charset="utf-8">
<title>KESTREL Business Card</title>
<link rel="stylesheet" href="https://fonts.googleapis.com/css2?family=Michroma&family=Questrial&display=swap">
<style>
  :root {
    --page: #ffffff;
    --ink: #000000;
    --paper: #ffffff;
    --rule: #5a5a5a;
  }
  html, body {
    margin: 0;
    padding: 0;
    width: 1200px;
    height: 1200px;
    overflow: hidden;
    background: var(--page);
  }
  .canvas {
    position: relative;
    width: 1200px;
    height: 1200px;
  }
  .card {
    position: absolute;
    left: 302px;
    width: 569px;
    height: 328px;
    box-sizing: border-box;
  }
  .card--front {
    top: 261px;
    background: var(--ink);
    display: flex;
    align-items: center;
    justify-content: center;
  }
  .card--back {
    top: 673px;
    background: var(--paper);
    border: 1.5px solid var(--rule);
  }
  .brand-name {
    font-family: "Michroma", sans-serif;
    font-weight: 400;
    letter-spacing: 0.3em;
    margin: 0;
  }
  .card--front .brand-name {
    color: var(--paper);
    font-size: 46px;
    padding-left: 0.3em;
  }
  .card--back .brand-name {
    position: absolute;
    left: 295px;
    top: 200px;
    width: 240px;
    text-align: center;
    color: var(--ink);
    font-size: 26px;
    padding-left: 0.3em;
    box-sizing: border-box;
  }
  .contact {
    position: absolute;
    left: 43px;
    top: 70px;
    color: var(--ink);
  }
  .contact__name {
    font-family: "Michroma", sans-serif;
    font-size: 24px;
    letter-spacing: 0.04em;
    margin: 0 0 20px;
  }
  .contact__block {
    font-family: "Questrial", sans-serif;
    font-size: 21px;
    line-height: 27px;
    margin: 0 0 27px;
  }
</style>
</head>
<body>
<main class="canvas">
  <section class="card card--front">
    <p class="brand-name">KESTREL</p>
  </section>

  <section class="card card--back">
    <div class="contact">
      <h1 class="contact__name">JOHN DOE</h1>
      <p class="contact__block">333 address<br>city, state, 55555</p>
      <p class="contact__block">555.555.5555<br>JDoe@website.com<br>www.website.com</p>
    </div>
    <p class="brand-name">KESTREL</p>
  </section>
</main>
</body>
</html>
```